Fresh, modern, fun business card for pediatric dental practice

Need a business card for fresh, modern, fun pediatric dental practice

Clean look that matches our website's font and colors

We prefer the look of curved corners on business cards

Target Market(s)

parents (mothers) of young children, professionals, mid-high class

Industry/Entity Type

Dental

Contact Information for Business Card

Maplewood Pediatric Dentistry
482 Corbett Lane
Suite 619
Alderton, PA 17999
717.555.0193
www.maplewoodtotsdental.example

Mei-Hua Tran, DMD
Colette Margrave, DMD
(we are working on our email address, but we would like that on the card as well)

Font styles to use
Sans Serif

Requirements
Must have
• All info; we would also like to make cards for individual staff members
• colors from our website and color palatte, attatched
• use same font and design as website for branding
Nice to have
• clean, simple card that has a pop of color
• we would like to see a few designs with our tag line "where smiles get brighter"
• we are not sure if we want to have it on there or not
• we would like to see a few designs incorporating the ribbon graphic on our website where the word WELCOME is

```html
<!DOCTYPE html>
<html lang="en">
<head>
<meta charset="utf-8">
<title>Maplewood Pediatric Dentistry – Business Card</title>
<link rel="stylesheet" href="https://fonts.googleapis.com/css2?family=Source+Sans+3:wght@400;600&display=swap">
<style>
  :root {
    --sun-yellow: #fbc02d;
    --sun-yellow-soft: #ecc22e;
    --sun-yellow-deep: #f0b628;
    --gold: #dea600;
    --logo-gold: #f5b400;
    --magenta: #e04ae8;
    --white: #ffffff;
    --mist-top: #ffffff;
    --mist-bottom: #e8ebeb;
    --slate: #c3d0d0;
    --ribbon: #adada8;
    --ribbon-ink: #4b2a66;
    --ribbon-ink-soft: #6c3b8c;
    --faint-mark: rgba(205, 120, 60, 0.28);
  }
  * { box-sizing: border-box; margin: 0; padding: 0; }
  html, body {
    width: 1200px; height: 720px; overflow: hidden;
    background: var(--white);
    font-family: "Source Sans 3", "Myriad Pro", Arial, sans-serif;
  }
  .card { position: relative; width: 1200px; height: 720px; overflow: hidden; background: var(--sun-yellow); }

  .header { position: absolute; left: 0; top: 0; width: 1200px; height: 291px; }
  .header svg { position: absolute; inset: 0; }

  .brand {
    position: absolute; left: 0; top: 92px; width: 1200px;
    display: flex; flex-direction: column; align-items: center;
  }
  .brand-dot {
    width: 62px; height: 62px; border-radius: 50%;
    background: var(--logo-gold); margin-bottom: 18px;
  }
  .brand-name {
    color: var(--logo-gold); font-weight: 600; text-align: center;
    font-size: 60px; line-height: 1; letter-spacing: 1px;
  }
  .brand-name span { display: block; font-size: 31px; letter-spacing: 2px; margin-top: 6px; }

  .stripe { position: absolute; left: 0; width: 1200px; height: 20px; background: var(--magenta); }
  .stripe--upper { top: 291px; }
  .stripe--lower { top: 556px; }

  .panel {
    position: absolute; left: 0; top: 310px; width: 1200px; height: 246px;
    background: var(--gold);
    box-shadow: 0 3px 4px rgba(80, 30, 90, 0.45), 0 -3px 4px rgba(80, 30, 90, 0.35);
    color: var(--white);
  }
  .panel-mark {
    position: absolute; left: 935px; top: 55px; width: 140px; height: 140px;
    border-radius: 50%; background: var(--faint-mark);
  }
  .doctor {
    position: absolute; left: 0; top: 44px; width: 1200px; text-align: center;
    font-size: 39px; font-weight: 400; letter-spacing: 0.3px;
  }
  .contact { position: absolute; display: flex; align-items: center; gap: 12px; font-size: 24px; }
  .contact svg { width: 28px; height: 28px; flex: none; }
  .contact--phone { left: 335px; top: 128px; }
  .contact--email { left: 593px; top: 128px; }
  .contact--web { left: 415px; top: 194px; }

  .footer { position: absolute; left: 0; top: 576px; width: 1200px; height: 91px; background: var(--slate); }
  .ribbon { position: absolute; left: 310px; top: 9px; width: 610px; height: 77px; }
  .ribbon svg { position: absolute; inset: 0; }
  .ribbon-text {
    position: absolute; left: 0; top: 8px; width: 572px; text-align: center;
    line-height: 1.22;
  }
  .ribbon-title { color: var(--ribbon-ink); font-size: 24px; font-weight: 600; }
  .ribbon-address { color: var(--ribbon-ink-soft); font-size: 24.5px; font-weight: 400; }

  .base { position: absolute; left: 0; top: 667px; width: 1200px; height: 53px; background: var(--sun-yellow-soft); }
  .base-tab { position: absolute; left: 0; top: 0; width: 66px; height: 53px; background: var(--sun-yellow-deep); }
</style>
</head>
<body>
<div class="card">
  <header class="header">
    <svg width="1200" height="291" viewBox="0 0 1200 291" aria-hidden="true">
      <defs>
        <linearGradient id="mist" x1="0" y1="0" x2="0" y2="1">
          <stop offset="0" stop-color="var(--mist-top)"/>
          <stop offset="1" stop-color="var(--mist-bottom)"/>
        </linearGradient>
      </defs>
      <rect width="1200" height="291" fill="var(--sun-yellow)"/>
      <path d="M0 52 Q600 112 1200 52 L1200 291 L0 291 Z" fill="url(#mist)"/>
    </svg>
    <div class="brand">
      <div class="brand-dot"></div>
      <div class="brand-name">maplewood<span>pediatric dentistry</span></div>
    </div>
  </header>

  <div class="stripe stripe--upper"></div>

  <section class="panel">
    <div class="panel-mark"></div>
    <h1 class="doctor">MEI-HUA TRAN, DMD</h1>
    <div class="contact contact--phone">
      <svg viewBox="0 0 28 28" aria-hidden="true">
        <circle cx="14" cy="14" r="12.5" fill="none" stroke="#fff" stroke-width="2"/>
        <path d="M9.5 8 l3 0 l1 3.5 l-1.8 1.3 q1.4 2.9 4.5 4.5 l1.3-1.8 l3.5 1 l0 3 q-1 1.2-2.5 1 q-9.5-2-10-10.5 q0-1.3 1-2z" fill="#fff"/>
      </svg>
      <span>717.555.0193</span>
    </div>
    <div class="contact contact--email">
      <svg viewBox="0 0 28 28" aria-hidden="true">
        <circle cx="14" cy="14" r="12.5" fill="none" stroke="#fff" stroke-width="2"/>
        <rect x="8" y="9.5" width="12" height="9" fill="#fff"/>
        <path d="M8 9.5 l6 5 l6-5" fill="none" stroke="var(--gold)" stroke-width="1.3"/>
      </svg>
      <span>info@maplewood.example</span>
    </div>
    <div class="contact contact--web">
      <svg viewBox="0 0 28 28" aria-hidden="true">
        <circle cx="14" cy="14" r="12.5" fill="none" stroke="#fff" stroke-width="2"/>
        <circle cx="14" cy="14" r="7.5" fill="#fff"/>
        <path d="M10 10 q3 1 2 4 q2 1 1 4 M16 8 q-1 3 2 4 q2 0 2 2" fill="none" stroke="var(--gold)" stroke-width="1.3"/>
      </svg>
      <span>www.maplewoodtotsdental.example</span>
    </div>
  </section>

  <div class="stripe stripe--lower"></div>

  <footer class="footer">
    <div class="ribbon">
      <svg width="610" height="77" viewBox="0 0 610 77" aria-hidden="true">
        <path d="M0 0 H610 L565 38.5 L610 77 H0 Z" fill="var(--ribbon)"/>
      </svg>
      <div class="ribbon-text">
        <p class="ribbon-title">MAPLEWOOD PEDIATRIC DENTISTRY</p>
        <p class="ribbon-address">482 Corbett Lane Suite 619 Alderton, PA 17999</p>
      </div>
    </div>
  </footer>

  <div class="base"><div class="base-tab"></div></div>
</div>
</body>
</html>
```